Graphic Design for a block-note A4 size

We need a graphic design for a simple block-note A4 size. The product consists of 50 sheets in VERTICAL A4 (21x29,7cm) size, simply glued on top, without cover. We would like to have proposals with double application: one for home users without a logo and one for professionals with an area "put your logo here".
The graphics should be simple and attractive, elegant and pleasant to keep on your desk.
The block-notes may have standard squares (5 or 10 mm) or stripes (10 mm spaced) on the background to make the writing easy.
Feel free to use your creativity, the only limit is the CMYK color space.

We will upload some block-note simple templates and 3D sample images to help you.

Reason: We want to give you more few days to work on your graphic designs.

Industry/Entity Type

Graphic Design

Requirements
Must have
• The graphics should be simple and attractive, elegant and pleasant to keep on your desk.

Nice to have
• The block-notes may have standard squares (5 or 10 mm) or stripes (10 mm spaced) on the background to make the writing easy.

```html
<!DOCTYPE html>
<html lang="en">
<head>
<meta charset="utf-8">
<title>A4 Lined Notepad Sheet</title>
<link rel="stylesheet" href="https://fonts.googleapis.com/css2?family=Arimo:wght@700&display=swap">
<style>
  :root {
    --paper: #ffffff;
    --frame-yellow: #f6c200;
    --frame-yellow-deep: #f0b400;
    --rule-grey: #b4b4b4;
    --mark-ink: #3a3a3a;
  }
  html, body {
    margin: 0;
    padding: 0;
    width: 853px;
    height: 1200px;
    overflow: hidden;
    background: var(--paper);
  }
  .sheet {
    position: relative;
    width: 853px;
    height: 1200px;
    background: var(--paper);
    overflow: hidden;
  }
  .sheet__frame {
    position: absolute;
    inset: 0;
    width: 853px;
    height: 1200px;
  }
  .sheet__rules {
    position: absolute;
    left: 34px;
    right: 34px;
    top: 128px;
    height: 932px;
    background-image: repeating-linear-gradient(
      to bottom,
      var(--rule-grey) 0,
      var(--rule-grey) 1px,
      transparent 1px,
      transparent 35.8px
    );
  }
  .sheet__mark {
    position: absolute;
    right: 44px;
    top: 1090px;
    height: 40px;
    display: flex;
    align-items: center;
    gap: 12px;
  }
  .sheet__mark-square {
    width: 22px;
    height: 22px;
    background: var(--frame-yellow);
  }
  .sheet__mark-name {
    font-family: "Arimo", Arial, sans-serif;
    font-weight: 700;
    font-size: 26px;
    line-height: 1;
    color: var(--mark-ink);
    margin: 0;
    white-space: nowrap;
  }
</style>
</head>
<body>
  <main class="sheet">
    <svg class="sheet__frame" viewBox="0 0 853 1200" role="img" aria-label="Rough yellow painted brush-stroke border framing the page">
      <defs>
        <linearGradient id="frameTone" x1="0" y1="0" x2="1" y2="1">
          <stop offset="0" stop-color="#f6c200"/>
          <stop offset="1" stop-color="#f0b400"/>
        </linearGradient>
      </defs>
      <path fill="url(#frameTone)" fill-rule="evenodd"
        d="M0 0 H853 V1200 H0 Z
           M28 60 H826 V1150 H28 Z"/>
    </svg>

    <div class="sheet__rules" aria-hidden="true"></div>

    <div class="sheet__mark">
      <span class="sheet__mark-square" aria-hidden="true"></span>
      <p class="sheet__mark-name">Your Mark</p>
    </div>
  </main>
</body>
</html>
```